A book about police officer shootings needs a dynamic cover design

I've almost completed a book on officer involved shootings...a very hot topic today. The title is "R.K.T. Beyond The Silence Fell." (emphasis on "beyond the silence") It details three separate shooting incidents, all within the same law enforcement family.I need a professional looking book cover that helps capture the drama. I attached a file of something I put together that is close, but I am concerned about "readability" and want a more professional look. I included a photo that I took off the internet of a gun being shot. That particular photo can stay or go, or be altered, but I like the perspective of the photo being fired from the person behind it. I wanted the cover to have the characteristics and color of a police uniform, utilizing blues, silvers, and maybe a little gold. I'm concerned about making sure the font and colors are also easy to read. I also will be working on a website design for "Beyond The Silence.Com" once the book hits the market. The back cover will incorporate the same colors, but only be a picture and excerpts from the book. I've included both for your review.

Target Market(s)

Law Enforcement, Christian, Media

Font styles to use
Sans Serif

Requirements
Must have
• A professional and readable appearance, that captures the drama of the topic. All the wording on the sample cover I attached, unless you come up with something better. A gun being fired from the perspective of the officer pulling the trigger. The size of the book will be the standard 6 x 9 in size. "Beyond The Silence" will eventually be my website domain and social media promotion hashtag.
Nice to have
• I would like the cover to incorporate the colors of a police uniform and badge, traditionally, navy blue, silver and some gold.
Should not have
• No police badge with a black band across. Not my topic.

```html
<!DOCTYPE html>
<html lang="en">
<head>
<meta charset="utf-8">
<title>R.K.T. Beyond The Silence Fell — Book Cover</title>
<link rel="stylesheet" href="https://fonts.googleapis.com/css2?family=Anton&family=Oswald:wght@500;700&family=Roboto:ital,wght@0,400;1,400&display=swap">
<style>
  :root {
    --navy: #0a0e1c;
    --navy-mid: #1b2a6b;
    --police-blue: #2b4fd8;
    --sky: #cfe3f4;
    --red: #e1141b;
    --yellow: #fff200;
    --white: #ffffff;
    --ink: #111111;
    --wood: #7a2f1d;
    --gold: #c9a24a;
  }
  * { box-sizing: border-box; margin: 0; padding: 0; }
  html, body { width: 1200px; height: 1000px; overflow: hidden; background: var(--white); }
  .stage { position: relative; width: 1200px; height: 1000px; }

  .cover { position: absolute; top: 50px; width: 494px; height: 745px; overflow: hidden; background: var(--navy); }
  .cover--front { left: 60px; }
  .cover--back { left: 615px; }

  /* front */
  .front-photo {
    position: absolute; left: 0; top: 0; width: 100%; height: 610px;
    background: linear-gradient(180deg, var(--white) 0%, var(--sky) 18%, #8fb5d8 35%, #1a1f33 45%, var(--police-blue) 60%, #a9c6f5 75%, var(--navy-mid) 100%);
  }
  .tagline {
    position: absolute; top: 26px; left: 0; width: 100%; text-align: center;
    font: 500 18px/1 "Oswald", sans-serif; color: var(--ink); letter-spacing: 0.3px;
  }
  .title { position: absolute; z-index: 3; font-family: "Anton", sans-serif; line-height: 0.9; text-transform: uppercase; white-space: nowrap; }
  .title--acronym { left: 42px; top: 312px; font-size: 40px; color: var(--white); -webkit-text-stroke: 1.5px var(--ink); }
  .title--lead { left: 30px; top: 356px; font-size: 54px; color: var(--red); -webkit-text-stroke: 1.5px var(--ink); }
  .title--main { left: 36px; top: 412px; font-size: 124px; color: var(--red); -webkit-text-stroke: 2px var(--ink); }
  .title--end { left: 280px; top: 528px; font-size: 68px; color: var(--yellow); -webkit-text-stroke: 1.5px var(--ink); }

  .band {
    position: absolute; z-index: 2; background: var(--yellow); color: var(--ink);
    font: 500 22px/1.1 "Oswald", sans-serif; text-transform: uppercase; text-align: left; white-space: nowrap;
  }
  .band .accent { color: var(--red); }
  .band .line { display: block; }
  .band--front { left: -10px; top: 578px; width: 510px; height: 86px; padding: 12px 0 0 30px; transform: rotate(2deg); }
  .band--front .line--second { padding-left: 78px; }

  .gavel { position: absolute; z-index: 1; background: linear-gradient(135deg, var(--wood), #3b140b 60%, var(--gold)); border-radius: 6px; }
  .gavel--front { left: 10px; top: 672px; width: 150px; height: 73px; }
  .author {
    position: absolute; left: 190px; top: 690px; width: 240px; text-align: center;
    font: 700 28px/1 "Oswald", sans-serif; color: var(--white); letter-spacing: 0.5px;
  }

  /* back */
  .back-photo {
    position: absolute; left: 0; top: 0; width: 100%; height: 300px;
    background: linear-gradient(120deg, #2d3f9a 0%, var(--police-blue) 35%, #6f3a7a 60%, #c25a3a 80%, #e6e6f0 100%);
    clip-path: polygon(0 0, 100% 0, 100% 52%, 0 100%);
  }
  .back-title { position: absolute; z-index: 3; font-family: "Anton", sans-serif; line-height: 0.9; text-transform: uppercase; white-space: nowrap; }
  .back-title--lead { left: 46px; top: 30px; font-size: 50px; color: var(--white); -webkit-text-stroke: 1px var(--ink); }
  .back-title--main { left: 46px; top: 78px; font-size: 86px; color: var(--red); -webkit-text-stroke: 1.5px var(--ink); }
  .back-title--end { left: 272px; top: 158px; font-size: 48px; color: var(--yellow); -webkit-text-stroke: 1px var(--ink); }
  .gavel--back { left: 35px; top: 178px; width: 80px; height: 52px; }
  .band--back { left: 38px; top: 222px; width: 322px; height: 52px; padding: 5px 0 0 14px; font-size: 20px; line-height: 1.05; transform: rotate(-5deg); }
  .band--back .line--second { padding-left: 22px; }

  .pull-quote {
    position: absolute; right: 30px; top: 280px; width: 300px; text-align: right;
    font: italic 400 15px/1.35 "Roboto", sans-serif; color: var(--yellow);
  }
  .story { position: absolute; left: 25px; width: 445px; display: flex; gap: 10px; }
  .story--one { top: 330px; }
  .story--two { top: 430px; }
  .story--three { top: 535px; }
  .portrait { flex: 0 0 55px; height: 70px; margin-top: 8px; background: linear-gradient(180deg, #c9d2dc, #6d7f94); }
  .story-heading { font: 700 17px/1.2 "Oswald", sans-serif; color: var(--white); text-transform: uppercase; }
  .story-text { font: 400 10.5px/1.3 "Roboto", sans-serif; color: var(--white); margin-top: 2px; }

  .imprint { position: absolute; left: 32px; top: 670px; font: 400 12px/1.4 "Roboto", sans-serif; color: var(--white); }
  .code-box { position: absolute; left: 283px; top: 647px; width: 180px; height: 69px; background: var(--white); }
</style>
</head>
<body>
<main class="stage">
  <section class="cover cover--front">
    <div class="front-photo" role="img" aria-label="Photo of a handgun being fired, seen from behind the officer's hands, over blue police lights"></div>
    <p class="tagline">IT WILL HAPPEN, AND IT WILL COME OUT OF NOWHERE...</p>
    <h1>
      <span class="title title--acronym">R.K.T.</span>
      <span class="title title--lead">Beyond The</span>
      <span class="title title--main">Silence</span>
      <span class="title title--end">Fell</span>
    </h1>
    <p class="band band--front"><span class="line">One <span class="accent">Law</span> Enforcement Family...</span><span class="line line--second">Three Life-Changing Stories</span></p>
    <div class="gavel gavel--front" role="img" aria-label="Illustration of a wooden judge's gavel with gold band"></div>
    <p class="author">LT. DAN MARLOW</p>
  </section>

  <section class="cover cover--back">
    <div class="back-photo" role="img" aria-label="Blurred photo of police lights with a gun sight crosshair"></div>
    <h2>
      <span class="back-title back-title--lead">Beyond The</span>
      <span class="back-title back-title--main">Silence</span>
      <span class="back-title back-title--end">Fell</span>
    </h2>
    <div class="gavel gavel--back" role="img" aria-label="Illustration of a wooden judge's gavel"></div>
    <p class="band band--back"><span class="line">One <span class="accent">Law</span> Enforcement Family...</span><span class="line line--second">Three Life-Changing Stories</span></p>

    <p class="pull-quote">“You cannot rely on anyone<br>but yourself to save your life…”</p>

    <article class="story story--one">
      <div class="portrait" role="img" aria-label="Portrait photo of Dan"></div>
      <div>
        <h3 class="story-heading">Dan's Story</h3>
        <p class="story-text">“And then I heard it. The unmistakable sound of a shotgun being racked. And then another one. I was hit with near-blinding light from police flashlights, but was still able to make out the silhouettes of officers taking cover behind their patrol car doors... All weapons pointed directly at me…”</p>
      </div>
    </article>
    <article class="story story--two">
      <div class="portrait" role="img" aria-label="Portrait photo of Corey"></div>
      <div>
        <h3 class="story-heading">Corey's Story</h3>
        <p class="story-text">“Corey stood over him, holding the shotgun in his left hand and his now empty handgun in his right. He stood there in stunned disbelief at how a routine call had escalated into a violent confrontation in a matter of seconds. The stench emanating from the house, mixed with the smell of gunpowder and blood, was almost overwhelming.”</p>
      </div>
    </article>
    <article class="story story--three">
      <div class="portrait" role="img" aria-label="Portrait photo of Grant"></div>
      <div>
        <h3 class="story-heading">Grant's Story</h3>
        <p class="story-text">“Grant desperately wanted to stay with Neil, but the danger still presented by Haskell was paramount. As Grant rushed towards the suspended vehicle, the door suddenly opened. Haskell climbed out and dropped to the ground. He stood and faced Grant like a raging bull. If the bull charged, Grant was prepared to shoot again…”</p>
      </div>
    </article>

    <p class="imprint">www.beyondthesilence.com<br>More info goes here</p>
    <div class="code-box"></div>
  </section>
</main>
</body>
</html>
```